Skyward Rovers

I would like to re-fresh my existing web page with something more elegant and professional and what will match with my new logo. From the page it should be clearly seen that I organize and sell flying safaris, it should not be tightened only to Africa, should be general.

Page to be re-freshed:
http://skyward-rovers.example

Target Market(s)

Pilots and non-pilots who are going to have a bush flying safari in Africa

Industry/Entity Type

It Professional

```html
<!DOCTYPE html>
<html lang="en">
<head>
<meta charset="utf-8">
<title>Skyward Rovers – Flying Safaris</title>
<link href="https://fonts.googleapis.com/css2?family=Source+Sans+3:wght@400;700&family=Fira+Sans+Condensed:wght@400;600&display=swap" rel="stylesheet">
<style>
  :root {
    --page-bg: #f2f3f2;
    --ink: #2f2f2f;
    --body-ink: #3a3a3a;
    --rule: #c9cbc9;
    --nav-active: #e4e5e4;
    --accent-orange: #f26b0f;
    --olive: #7b8a1d;
    --crimson: #951111;
    --brown: #6b4527;
    --white: #ffffff;
    --dot-active: #d0262b;
  }
  * { box-sizing: border-box; margin: 0; padding: 0; }
  html, body { width: 953px; height: 1200px; overflow: hidden; }
  body {
    position: relative;
    background: var(--page-bg);
    font-family: "Source Sans 3", sans-serif;
    color: var(--ink);
  }
  .brand {
    position: absolute; left: 108px; top: 50px;
    display: flex; align-items: center; gap: 12px;
  }
  .brand-mark { width: 56px; height: 56px; border-radius: 50%; background: var(--ink); }
  .brand-name { font-size: 36px; font-weight: 400; color: var(--ink); line-height: 1; }

  .utility-nav {
    position: absolute; left: 763px; top: 47px;
    font-family: "Fira Sans Condensed", sans-serif; font-size: 10px;
    color: #777; display: flex; gap: 11px;
  }
  .search { position: absolute; left: 594px; top: 86px; display: flex; gap: 8px; }
  .search-field {
    width: 185px; height: 17px; border: 1px solid #b5b7b5; border-radius: 3px;
    background: linear-gradient(#e6e7e6, #fff); position: relative;
  }
  .search-field svg { position: absolute; left: 5px; top: 3px; }
  .search-button {
    width: 60px; height: 17px; border: 1px solid #b5b7b5; border-radius: 2px;
    background: linear-gradient(#fff, #dcdddc);
    font-family: "Fira Sans Condensed", sans-serif; font-size: 9px;
    display: flex; align-items: center; justify-content: center; color: #333;
  }

  .main-nav {
    position: absolute; left: 103px; top: 126px; width: 744px; height: 31px;
    border: 1px solid var(--rule); background: var(--white);
    display: flex; align-items: center;
    font-size: 12px; color: var(--ink);
  }
  .main-nav a {
    height: 100%; display: flex; align-items: center; justify-content: center;
    padding-top: 3px;
    text-decoration: none; color: inherit; border-right: 1px solid var(--rule);
  }
  .main-nav a:last-child { border-right: none; }
  .main-nav .active { background: var(--nav-active); }
  .main-nav .small { font-size: 10.5px; padding-top: 1px; }

  .hero {
    position: absolute; left: 103px; top: 174px; width: 743px; height: 333px;
    border: 1px solid #b9bbb9;
  }
  .hero-photo {
    width: 100%; height: 100%;
    background:
      radial-gradient(ellipse at 30% 45%, #c9772c 0%, #9a4e18 35%, transparent 60%),
      linear-gradient(90deg, #7a3d12 0%, #a3561c 30%, #4d3a1c 60%, #2a2a14 100%);
  }
  .hero-copy {
    position: absolute; left: 453px; top: 78px;
    font-family: "Fira Sans Condensed", sans-serif; font-size: 27px; line-height: 39px;
    color: var(--white);
  }
  .hero-copy .highlight { color: var(--accent-orange); font-weight: 600; }
  .hero-arrow { position: absolute; top: 313px; width: 33px; height: 33px; }
  .hero-arrow.prev { left: 85px; }
  .hero-arrow.next { left: 832px; }
  .hero-dots { position: absolute; left: 663px; top: 311px; display: flex; gap: 3px; }
  .hero-dots span { width: 8px; height: 8px; border-radius: 50%; background: #e8e6dc; }
  .hero-dots span.on { background: var(--dot-active); }

  .copy {
    position: absolute; left: 103px; width: 745px;
    font-size: 14.6px; line-height: 18px; color: var(--body-ink);
  }
  .intro { top: 523px; }
  .intro strong { color: #111; }
  .para-two { top: 823px; }
  .para-three { top: 965px; }

  .tour-card {
    position: absolute; top: 622px; width: 178px; height: 188px;
    border: 1px solid var(--rule); background: var(--white);
  }
  .tour-card h2 {
    margin: 2px; height: 29px; display: flex; align-items: center; justify-content: center;
    font-family: "Fira Sans Condensed", sans-serif; font-weight: 400; font-size: 12px;
    color: var(--white); border: 1px solid rgba(0,0,0,0.15);
  }
  .tour-card .tour-photo { position: absolute; left: 0; top: 34px; width: 176px; height: 152px; }
  .card-guided { left: 103px; } .card-guided h2 { background: var(--olive); }
  .card-self { left: 292px; } .card-self h2 { background: var(--accent-orange); }
  .card-sample { left: 480px; } .card-sample h2 { background: var(--crimson); }
  .card-build { left: 669px; } .card-build h2 { background: var(--brown); }
  .card-guided .tour-photo { background: linear-gradient(#5a86c8 0%, #9fc0e6 45%, #d9cdb3 60%, #c8b89a 100%); }
  .card-self .tour-photo { background: linear-gradient(135deg, #b9a68d 0%, #efe8df 45%, #d8cfc2 70%, #a89a84 100%); }
  .card-sample .tour-photo { background: linear-gradient(#6d7a4a 0%, #8c8a5a 45%, #a88d5e 75%, #8a7a5c 100%); }
  .card-build .tour-photo { background: linear-gradient(#8f5e39 0%, #b98358 45%, #5d3b24 75%, #2e2017 100%); }

  .follow {
    position: absolute; left: 706px; top: 1105px; width: 143px; height: 60px;
    border: 1px solid #d8d9d8; border-radius: 3px; background: #f7f7f7;
    padding: 2px 7px;
  }
  .follow-title { font-size: 16px; color: #333; line-height: 20px; }
  .follow-links { display: flex; gap: 3px; margin-top: 3px; }
  .follow-links span { width: 30px; height: 30px; border-radius: 2px; }
  .s1 { background: #d44633; } .s2 { background: #c4302b; }
  .s3 { background: #3b5b99; } .s4 { background: #3fa9e0; }

  .copyright { position: absolute; left: 104px; top: 1150px; font-size: 12.5px; color: #111; }
</style>
</head>
<body>
  <header>
    <div class="brand">
      <div class="brand-mark"></div>
      <div class="brand-name">Skyward Rovers</div>
    </div>
    <nav class="utility-nav"><span>HOME</span><span>CONTACT US</span></nav>
    <div class="search">
      <div class="search-field">
        <svg width="10" height="10" viewBox="0 0 10 10"><circle cx="4" cy="4" r="3" fill="none" stroke="#777" stroke-width="1.2"/><line x1="6.2" y1="6.2" x2="9" y2="9" stroke="#777" stroke-width="1.4"/></svg>
      </div>
      <div class="search-button">SEARCH</div>
    </div>
    <nav class="main-nav">
      <a class="active" style="width:118px">GUIDED TOURS</a>
      <a style="width:138px">SELF GUIDED TOURS</a>
      <a style="width:113px">SAMPLE TOURS</a>
      <a style="width:123px">BUILD YOUR TRIP</a>
      <a class="small" style="width:66px">Training</a>
      <a class="small" style="width:98px">PPL Validation</a>
      <a class="small" style="width:64px">Gallery</a>
    </nav>
  </header>

  <section class="hero">
    <div class="hero-photo" role="img" aria-label="Close-up of a roaring lion against a blurred savanna background"></div>
    <p class="hero-copy">Welcome to the<br><span class="highlight">WORLD OF SKYWARD</span><br>rovers for the<br>adventure of a lifetime</p>
    <div class="hero-dots"><span class="on"></span><span></span><span></span><span></span><span></span></div>
  </section>
  <svg class="hero-arrow prev" viewBox="0 0 33 33"><circle cx="16.5" cy="16.5" r="15.5" fill="#f4f4f4" stroke="#bbb"/><circle cx="16.5" cy="16.5" r="12" fill="#fff" stroke="#ddd"/><path d="M19 11 L12 16.5 L19 22 Z" fill="#666"/></svg>
  <svg class="hero-arrow next" viewBox="0 0 33 33"><circle cx="16.5" cy="16.5" r="15.5" fill="#f4f4f4" stroke="#bbb"/><circle cx="16.5" cy="16.5" r="12" fill="#fff" stroke="#ddd"/><path d="M14 11 L21 16.5 L14 22 Z" fill="#666"/></svg>

  <p class="copy intro"><strong>Skyward Rovers</strong> plans and sells flying safaris to the wildest corners of the world. What better way to see the wonders of remote lands than from the pilot's seat of your own aircraft? Whether you're a PPL wanting to experience something beyond flying circuits at your local airfield, a seasoned ATP looking to recapture that passion for flying, or a traveller wanting to see the wilderness from a bird's perspective, alone or as part of a group, a flying safari offers a truly rewarding and unforgettable experience.</p>

  <article class="tour-card card-guided"><h2>GUIDED TOURS</h2><div class="tour-photo" role="img" aria-label="Light aircraft parked on a bush airstrip under a blue sky"></div></article>
  <article class="tour-card card-self"><h2>SELF GUIDED TOURS</h2><div class="tour-photo" role="img" aria-label="White lion cub resting on sand"></div></article>
  <article class="tour-card card-sample"><h2>SAMPLE TOURS</h2><div class="tour-photo" role="img" aria-label="Giraffe beside a safari vehicle on a dirt road"></div></article>
  <article class="tour-card card-build"><h2>BUILD YOUR TRIP</h2><div class="tour-photo" role="img" aria-label="Impala drinking at a waterhole"></div></article>

  <p class="copy para-two">The most pristine and unspoiled places on earth are without doubt off the beaten track, often only accessible by air. If it's a genuine rustic and wild experience you're after, the adventures are only waiting, but you will not find them in any guidebook or airport listing. For a pilot, as for anyone else, these adventures come at a price: remote strips and the lack of the creature comforts we've gotten so used to (air traffic control, windsocks, tarmac, avgas, aircraft mechanics etc.), not to mention unpredictable weather and far distances from help. That is where we come in. We handle the routes, permits, fuel, lodges and local guides, so you can enjoy the rugged, romantic spirit of bush flying with great beauty, independence and peace of mind.</p>

  <p class="copy para-three">Whether setting out on your own or as part of an organised group, a safari by air is sure to be an adventure packed, rich and rewarding experience. From savannas and deltas to deserts, glaciers and rainforest coastlines, our destinations are chosen for their wildlife, cultures and stunning natural beauty. The mobility of flying lets you break away from the hustle and bustle of the normal tourist trail; the freedom of the air takes you to exclusive areas which are otherwise hard or nearly impossible to reach, places where the true wild still speaks in every sight and sound.</p>

  <footer>
    <div class="follow">
      <div class="follow-title">Follow Us</div>
      <div class="follow-links"><span class="s1"></span><span class="s2"></span><span class="s3"></span><span class="s4"></span></div>
    </div>
    <p class="copyright">Copyright © 2012-2013 skyward-rovers.example</p>
  </footer>
</body>
</html>
```